Movie Showtimes Website needs an updated new look

Website = www.marlovista.com

We want to update the look of our website. We want our website to look modern, trendy, something that was designed in 2018.

We don't need any HTML or CSS or web development. All we need is the graphical prototype, preferably in Photoshop with layers.

Most of our visitors use mobile devices. Our website is RESPONSIVE -- it is flexible to fit all screen sizes.

We will use this new logo (designed on Quillbarn):
https://www.quillbarn.com/design/27364512

Thank you for your kind consideration.

Please find attached 3 PDF files with the current webpages:

1. Each city location has its own HOME PAGE like this:

https://www.marlovista.com/ont/ottawa/

2. The most visited pages have movie SHOWTIMES and look like this:

https://www.marlovista.com/theatres/rovenna-hartfield-vip

MOVIE TITLE (poster + basic info + 4 buttons)
-- the type of the screening (ex. Regular, VYRA, 3D, etc.)
-- individual days and showtimes

3. INFORMATION about movies:

https://www.marlovista.com/movies/silent-copper-road-2018

Thank you.

Target Market(s)

Canada and USA, target audience = ages 13-50

Industry/Entity Type

Movie

Number of Pages Required

3 page

Font styles to use
Sans Serif

Colors

Designer to choose colors to be used in the design.

Requirements
Must have
• - For the main body text (such as movie times, description, information) we prefer dark text on a light background.
• - We will use the new logo https://www.quillbarn.com/design/27364512 -- but the text Marlo Vista in the logo doesn't have to look exactly like that, it can be on the same line and have the same or different size
Should not have
• No more than 2 different fonts (ex. one font for headers and titles, another one for text)

```html
<!DOCTYPE html>
<html lang="en">
<head>
<meta charset="utf-8">
<title>Marlo Vista – Movie Times</title>
<link rel="stylesheet" href="https://fonts.googleapis.com/css2?family=Poppins:wght@300;400;500;600&display=swap">
<style>
:root{
  --blue:#3eaaf0;
  --blue-dark:#2f95dc;
  --ink:#262d36;
  --ink-soft:#59616b;
  --muted:#9aa2ab;
  --line:#e7ebef;
  --page:#ffffff;
  --tint:#eef6fd;
  --tint-text:#c9dff2;
  --slate:#3c4550;
  --card-shadow:0 3px 14px rgba(30,50,80,.09);
}
*{box-sizing:border-box;margin:0;padding:0}
html,body{width:1200px;height:4072px;overflow:hidden}
body{position:relative;background:var(--page);font-family:"Poppins",sans-serif;color:var(--ink)}
.abs{position:absolute}

/* header */
.site-header{position:absolute;left:0;top:0;width:1200px;height:95px;background:#fff;display:flex;align-items:center}
.menu-icon{position:absolute;left:96px;top:38px;width:30px}
.menu-icon span{display:block;height:3px;background:var(--ink);margin-bottom:5px;border-radius:2px}
.brand{position:absolute;left:0;right:0;top:0;height:95px;display:flex;justify-content:center;align-items:center;gap:10px;font-weight:600;font-size:25px;letter-spacing:1px;color:var(--ink)}
.brand-dot{width:34px;height:34px;border-radius:50%;background:var(--ink)}
.header-tools{position:absolute;right:96px;top:0;height:95px;display:flex;align-items:center;gap:26px;font-size:14px}
.header-tools .signup{color:var(--blue)}
.header-tools .signin{color:var(--ink-soft)}

/* hero */
.hero{position:absolute;left:0;top:95px;width:1200px;height:312px;background:linear-gradient(100deg,#27b4d7 0%,#3a8fd1 45%,#5f6fc6 75%,#7a63be 100%)}
.hero-title{position:absolute;left:0;right:0;top:48px;text-align:center;color:#fff;font-weight:600;font-size:25px}
.choice-card{position:absolute;top:109px;width:488px;height:152px;background:#fff;border-radius:10px;box-shadow:0 6px 20px rgba(0,0,0,.12);display:flex;align-items:center;justify-content:center;gap:40px}
.choice-card svg{width:100px;height:80px}
.choice-label{text-align:center}
.choice-label small{display:block;font-size:17px;font-weight:500;letter-spacing:1px;color:var(--ink)}
.choice-label strong{display:block;font-size:38px;font-weight:600;color:var(--blue);line-height:1.1;letter-spacing:1px}

/* sections */
.section-title{position:absolute;left:0;right:0;text-align:center;font-weight:500;font-size:25px;color:var(--ink)}

/* movie grid */
.movie-grid{position:absolute;left:98px;top:540px;display:grid;grid-template-columns:488px 488px;column-gap:25px;row-gap:27px}
.movie-card{position:relative;width:488px;height:280px;background:#fff;border-radius:4px;box-shadow:var(--card-shadow)}
.poster{position:absolute;left:16px;top:10px;width:168px;height:260px}
.movie-info{position:absolute;left:198px;top:20px;right:16px}
.movie-title{font-size:19px;font-weight:600;display:flex;align-items:center;gap:8px;color:var(--ink)}
.rating-badge{font-size:10px;font-weight:600;color:#fff;background:var(--blue);border-radius:10px;padding:1px 9px}
.heart{position:absolute;right:16px;top:18px;width:24px;height:22px}
.movie-meta{font-size:12.5px;line-height:1.6;color:var(--ink-soft);margin-top:6px;width:250px}
.score{margin-top:14px;font-size:21px;font-weight:600;color:var(--blue);display:flex;align-items:center;gap:6px}
.score svg{width:17px;height:17px}
.movie-actions{position:absolute;left:198px;right:12px;bottom:14px;display:grid;grid-template-columns:repeat(4,1fr);text-align:center}
.action{position:relative;font-size:11px;color:var(--ink-soft)}
.action .count{position:absolute;right:4px;top:-26px;font-size:10px;color:var(--muted)}
.action svg{display:block;margin:0 auto 4px;width:20px;height:20px}

.pill{display:flex;align-items:center;justify-content:center;border-radius:30px;font-size:14px;font-weight:500;color:#fff}
.pill-blue{background:var(--blue);box-shadow:0 6px 14px rgba(62,170,240,.35)}
.pill-dark{background:var(--slate);box-shadow:0 6px 14px rgba(40,50,60,.3)}

/* promotions */
.promo-band{position:absolute;left:98px;top:2302px;width:1102px;height:399px;background:linear-gradient(90deg,var(--tint),#f6fafe)}
.promo-tag{position:absolute;left:105px;top:2500px;transform:translate(-50%,-50%) rotate(-90deg);font-size:44px;font-weight:500;letter-spacing:3px;color:var(--tint-text)}
.promo-poster{position:absolute;left:195px;top:2251px;width:337px;height:499px;border:6px solid #fff;box-shadow:0 10px 28px rgba(30,50,80,.2);background:linear-gradient(170deg,#f3f1ee 0%,#f0d8dc 45%,#f4b7c4 70%,#e9c25b 100%)}
.promo-copy{position:absolute;left:613px;top:2405px}
.promo-copy h3{font-size:42px;font-weight:500;color:var(--ink)}
.promo-copy p{font-size:17px;color:var(--ink-soft);margin-top:10px}
.promo-arrows{position:absolute;left:1050px;top:2646px;display:flex;gap:4px}

/* favourites */
.fav-sub{position:absolute;left:0;right:0;top:2890px;text-align:center;font-size:16px;color:var(--ink-soft)}
.ad{position:absolute;top:3111px;width:285px;height:239px}

/* birthdays */
.birthday-grid{position:absolute;left:98px;top:3516px;display:grid;grid-template-columns:repeat(3,315px);column-gap:29px;row-gap:28px}
.birthday-card{height:89px;background:#fff;border-radius:4px;box-shadow:var(--card-shadow);display:flex;align-items:center;gap:22px;padding-left:8px}
.avatar{width:76px;height:76px;border-radius:3px}
.birthday-card b{display:block;font-size:14px;font-weight:600;color:var(--ink)}
.birthday-card span{display:block;font-size:12px;color:var(--muted);margin-top:3px}

/* footer */
.site-footer{position:absolute;left:0;top:3945px;width:1200px;height:127px;background:var(--slate);color:#fff;font-size:13px}
.lang{position:absolute;left:96px;top:56px}
.copyright{position:absolute;left:0;right:0;top:56px;text-align:center}
.social{position:absolute;right:96px;top:48px;display:flex;gap:8px}
.social span{width:28px;height:28px;border:2px solid #fff;border-radius:50%}
</style>
</head>
<body>

<svg width="0" height="0" style="position:absolute">
  <defs>
    <symbol id="i-clock" viewBox="0 0 20 20"><circle cx="10" cy="10" r="8" fill="none" stroke="#59616b" stroke-width="1.4"/><path d="M10 5v5l3 2" fill="none" stroke="#59616b" stroke-width="1.4" stroke-linecap="round"/></symbol>
    <symbol id="i-info" viewBox="0 0 20 20"><circle cx="10" cy="10" r="8" fill="none" stroke="#59616b" stroke-width="1.4"/><path d="M10 9v5" stroke="#59616b" stroke-width="1.6" stroke-linecap="round"/><circle cx="10" cy="6" r="1" fill="#59616b"/></symbol>
    <symbol id="i-play" viewBox="0 0 20 20"><circle cx="10" cy="10" r="8" fill="none" stroke="#59616b" stroke-width="1.4"/><path d="M8 6.5l5 3.5-5 3.5z" fill="#59616b"/></symbol>
    <symbol id="i-list" viewBox="0 0 20 20"><path d="M3 5h14M3 10h14M3 15h9" stroke="#59616b" stroke-width="1.5" stroke-linecap="round"/></symbol>
    <symbol id="i-heart" viewBox="0 0 24 22"><path d="M12 20S2 13.5 2 7.2A5 5 0 0 1 12 5a5 5 0 0 1 10 2.2C22 13.5 12 20 12 20z" fill="none" stroke="#59616b" stroke-width="1.6"/></symbol>
    <symbol id="i-star" viewBox="0 0 20 20"><path d="M10 1.5l2.6 5.5 6 .7-4.4 4.1 1.2 5.9L10 14.8 4.6 17.7l1.2-5.9L1.4 7.7l6-.7z" fill="#b8bfc7"/></symbol>
  </defs>
</svg>

<header class="site-header">
  <div class="menu-icon"><span></span><span></span><span></span></div>
  <div class="brand"><span class="brand-dot"></span>MARLO VISTA</div>
  <nav class="header-tools">
    <svg width="16" height="16" viewBox="0 0 16 16"><circle cx="6.5" cy="6.5" r="5" fill="none" stroke="#262d36" stroke-width="1.8"/><path d="M10.5 10.5l4 4" stroke="#262d36" stroke-width="1.8" stroke-linecap="round"/></svg>
    <span class="signup">Sign Up</span>
    <span class="signin">Sign In</span>
  </nav>
</header>

<section class="hero" role="img" aria-label="Starry night sky backdrop in teal and violet">
  <h1 class="hero-title">Movie Times</h1>
  <a class="choice-card" style="left:98px">
    <svg viewBox="0 0 100 80"><path d="M12 42a38 24 0 0 1 76 0" fill="none" stroke="#3eaaf0" stroke-width="2.5"/><path d="M50 18v-12M30 22l-6-9M70 22l6-9M18 32l-9-5M82 32l9-5" stroke="#3eaaf0" stroke-width="2.5" stroke-linecap="round"/><rect x="10" y="42" width="80" height="22" fill="none" stroke="#3eaaf0" stroke-width="2.5"/><path d="M20 70h60" stroke="#3eaaf0" stroke-width="2.5"/></svg>
    <div class="choice-label"><small>CHOOSE A</small><strong>CINEMA</strong></div>
  </a>
  <a class="choice-card" style="left:611px">
    <svg viewBox="0 0 100 80"><circle cx="45" cy="40" r="32" fill="none" stroke="#3eaaf0" stroke-width="2.5"/><circle cx="45" cy="40" r="5" fill="none" stroke="#3eaaf0" stroke-width="2.5"/><circle cx="45" cy="22" r="8" fill="none" stroke="#3eaaf0" stroke-width="2.5"/><circle cx="45" cy="58" r="8" fill="none" stroke="#3eaaf0" stroke-width="2.5"/><circle cx="27" cy="40" r="8" fill="none" stroke="#3eaaf0" stroke-width="2.5"/><circle cx="63" cy="40" r="8" fill="none" stroke="#3eaaf0" stroke-width="2.5"/><path d="M45 72h45" stroke="#3eaaf0" stroke-width="2.5"/></svg>
    <div class="choice-label"><small>CHOOSE A</small><strong>MOVIE</strong></div>
  </a>
</section>

<h2 class="section-title" style="top:460px">New Movies This Week</h2>

<main class="movie-grid">
  <!-- row 1 -->
  <article class="movie-card">
    <div class="poster" role="img" aria-label="Poster for The Hollow Hush: dim grey house in the woods" style="background:linear-gradient(180deg,#4b5356,#2b3032 60%,#1c1f21)"></div>
    <svg class="heart"><use href="#i-heart"/></svg>
    <div class="movie-info">
      <h3 class="movie-title">The Hollow Hush <span class="rating-badge">14A</span></h3>
      <p class="movie-meta">1h30m • Horror/thriller • Dana Whitlock &amp; Owen Brask</p>
      <p class="score"><svg><use href="#i-star"/></svg>7.9</p>
    </div>
    <div class="movie-actions">
      <div class="action"><span class="count">5</span><svg><use href="#i-clock"/></svg>Times</div>
      <div class="action"><svg><use href="#i-info"/></svg>Info</div>
      <div class="action"><span class="count">7</span><svg><use href="#i-play"/></svg>Videos</div>
      <div class="action"><span class="count">86</span><svg><use href="#i-list"/></svg>Reviews</div>
    </div>
  </article>
  <article class="movie-card">
    <div class="poster" role="img" aria-label="Poster for Curfew Crashers: group of comic characters on black" style="background:linear-gradient(180deg,#1a1a1a,#3a2a22 55%,#8a5a3a)"></div>
    <svg class="heart"><use href="#i-heart"/></svg>
    <div class="movie-info">
      <h3 class="movie-title">Curfew Crashers <span class="rating-badge">14A</span></h3>
      <p class="movie-meta">1h42m • Comedy • Lena Marsh &amp; Jake Corbin</p>
      <p class="score"><svg><use href="#i-star"/></svg>7.3</p>
    </div>
    <div class="movie-actions">
      <div class="action"><span class="count">3</span><svg><use href="#i-clock"/></svg>Times</div>
      <div class="action"><svg><use href="#i-info"/></svg>Info</div>
      <div class="action"><span class="count">6</span><svg><use href="#i-play"/></svg>Videos</div>
      <div class="action"><span class="count">17</span><svg><use href="#i-list"/></svg>Reviews</div>
    </div>
  </article>
  <!-- row 2 -->
  <article class="movie-card">
    <div class="poster" role="img" aria-label="Poster for The Rally Season: athlete under a pink and teal sky" style="background:linear-gradient(160deg,#e87ab0,#b46fb8 40%,#3a9fb0 80%)"></div>
    <svg class="heart"><use href="#i-heart"/></svg>
    <div class="movie-info">
      <h3 class="movie-title">The Rally Season <span class="rating-badge">PG</span></h3>
      <p class="movie-meta">1h41m • Drama • Helen Varga &amp; Erin Tolland</p>
      <p class="score"><svg><use href="#i-star"/></svg>7.4</p>
    </div>
    <div class="movie-actions">
      <div class="action"><span class="count">6</span><svg><use href="#i-clock"/></svg>Times</div>
      <div class="action"><svg><use href="#i-info"/></svg>Info</div>
      <div class="action"><span class="count">3</span><svg><use href="#i-play"/></svg>Videos</div>
      <div class="action"><span class="count">12</span><svg><use href="#i-list"/></svg>Reviews</div>
    </div>
  </article>
  <article class="movie-card">
    <div class="poster" role="img" aria-label="Poster for La Rivière: dark period scene with warm lights" style="background:linear-gradient(180deg,#2a2623,#4a3b2f 60%,#1e1a17)"></div>
    <svg class="heart"><use href="#i-heart"/></svg>
    <div class="movie-info">
      <h3 class="movie-title">La Rivière <span class="rating-badge">PG</span></h3>
      <p class="movie-meta">1h43m • Comedy-drama • Julie Brassard &amp; Émile Tremblant</p>
      <p class="score"><svg><use href="#i-star"/></svg>8.0</p>
    </div>
    <div class="movie-actions">
      <div class="action"><span class="count">2</span><svg><use href="#i-clock"/></svg>Times</div>
      <div class="action"><svg><use href="#i-info"/></svg>Info</div>
      <div class="action"><span class="count">7</span><svg><use href="#i-play"/></svg>Videos</div>
      <div class="action"><span class="count">64</span><svg><use href="#i-list"/></svg>Reviews</div>
    </div>
  </article>
  <!-- row 3 -->
  <article class="movie-card">
    <div class="poster" role="img" aria-label="Poster for Harbor Bridge: pale sky over a dark bridge" style="background:linear-gradient(180deg,#e6e4df,#b9b6af 55%,#4a4a48)"></div>
    <svg class="heart"><use href="#i-heart"/></svg>
    <div class="movie-info">
      <h3 class="movie-title">Harbor Bridge <span class="rating-badge">14A</span></h3>
      <p class="movie-meta">1h47m • Dramatic thriller • Jason Orrell &amp; Kate Linden</p>
      <p class="score"><svg><use href="#i-star"/></svg>7.6</p>
    </div>
    <div class="movie-actions">
      <div class="action"><span class="count">4</span><svg><use href="#i-clock"/></svg>Times</div>
      <div class="action"><svg><use href="#i-info"/></svg>Info</div>
      <div class="action"><span class="count">7</span><svg><use href="#i-play"/></svg>Videos</div>
      <div class="action"><span class="count">80</span><svg><use href="#i-list"/></svg>Reviews</div>
    </div>
  </article>
  <article class="movie-card">
    <div class="poster" role="img" aria-label="Poster for Maîtresse: figures in an elegant grey interior" style="background:linear-gradient(180deg,#d9d6d1,#8c8782 50%,#2e2b29)"></div>
    <svg class="heart"><use href="#i-heart"/></svg>
    <div class="movie-info">
      <h3 class="movie-title">Maîtresse <span class="rating-badge">14A</span></h3>
      <p class="movie-meta">1h31m • Romance/thriller • Dana Whitlock &amp; Owen Brask</p>
      <p class="score"><svg><use href="#i-star"/></svg>7.9</p>
    </div>
    <div class="movie-actions">
      <div class="action"><span class="count">5</span><svg><use href="#i-clock"/></svg>Times</div>
      <div class="action"><svg><use href="#i-info"/></svg>Info</div>
      <div class="action"><span class="count">7</span><svg><use href="#i-play"/></svg>Videos</div>
      <div class="action"><span class="count">86</span><svg><use href="#i-list"/></svg>Reviews</div>
    </div>
  </article>
  <!-- row 4 -->
  <article class="movie-card">
    <div class="poster" role="img" aria-label="Poster for The Hollow Hush: dim grey house in the woods" style="background:linear-gradient(180deg,#4b5356,#2b3032 60%,#1c1f21)"></div>
    <svg class="heart"><use href="#i-heart"/></svg>
    <div class="movie-info">
      <h3 class="movie-title">The Hollow Hush <span class="rating-badge">14A</span></h3>
      <p class="movie-meta">1h30m • Horror/thriller • Dana Whitlock &amp; Owen Brask</p>
      <p class="score"><svg><use href="#i-star"/></svg>7.9</p>
    </div>
    <div class="movie-actions">
      <div class="action"><span class="count">5</span><svg><use href="#i-clock"/></svg>Times</div>
      <div class="action"><svg><use href="#i-info"/></svg>Info</div>
      <div class="action"><span class="count">7</span><svg><use href="#i-play"/></svg>Videos</div>
      <div class="action"><span class="count">86</span><svg><use href="#i-list"/></svg>Reviews</div>
    </div>
  </article>
  <article class="movie-card">
    <div class="poster" role="img" aria-label="Poster for Curfew Crashers: group of comic characters on black" style="background:linear-gradient(180deg,#1a1a1a,#3a2a22 55%,#8a5a3a)"></div>
    <svg class="heart"><use href="#i-heart"/></svg>
    <div class="movie-info">
      <h3 class="movie-title">Curfew Crashers <span class="rating-badge">14A</span></h3>
      <p class="movie-meta">1h42m • Comedy • Lena Marsh &amp; Jake Corbin</p>
      <p class="score"><svg><use href="#i-star"/></svg>7.3</p>
    </div>
    <div class="movie-actions">
      <div class="action"><span class="count">3</span><svg><use href="#i-clock"/></svg>Times</div>
      <div class="action"><svg><use href="#i-info"/></svg>Info</div>
      <div class="action"><span class="count">6</span><svg><use href="#i-play"/></svg>Videos</div>
      <div class="action"><span class="count">17</span><svg><use href="#i-list"/></svg>Reviews</div>
    </div>
  </article>
  <!-- row 5 -->
  <article class="movie-card">
    <div class="poster" role="img" aria-label="Poster for The Rally Season: athlete under a pink and teal sky" style="background:linear-gradient(160deg,#e87ab0,#b46fb8 40%,#3a9fb0 80%)"></div>
    <svg class="heart"><use href="#i-heart"/></svg>
    <div class="movie-info">
      <h3 class="movie-title">The Rally Season <span class="rating-badge">PG</span></h3>
      <p class="movie-meta">1h41m • Drama • Helen Varga &amp; Erin Tolland</p>
      <p class="score"><svg><use href="#i-star"/></svg>7.4</p>
    </div>
    <div class="movie-actions">
      <div class="action"><span class="count">6</span><svg><use href="#i-clock"/></svg>Times</div>
      <div class="action"><svg><use href="#i-info"/></svg>Info</div>
      <div class="action"><span class="count">3</span><svg><use href="#i-play"/></svg>Videos</div>
      <div class="action"><span class="count">12</span><svg><use href="#i-list"/></svg>Reviews</div>
    </div>
  </article>
  <article class="movie-card">
    <div class="poster" role="img" aria-label="Poster for La Rivière: dark period scene with warm lights" style="background:linear-gradient(180deg,#2a2623,#4a3b2f 60%,#1e1a17)"></div>
    <svg class="heart"><use href="#i-heart"/></svg>
    <div class="movie-info">
      <h3 class="movie-title">La Rivière <span class="rating-badge">PG</span></h3>
      <p class="movie-meta">1h43m • Comedy-drama • Julie Brassard &amp; Émile Tremblant</p>
      <p class="score"><svg><use href="#i-star"/></svg>8.0</p>
    </div>
    <div class="movie-actions">
      <div class="action"><span class="count">2</span><svg><use href="#i-clock"/></svg>Times</div>
      <div class="action"><svg><use href="#i-info"/></svg>Info</div>
      <div class="action"><span class="count">7</span><svg><use href="#i-play"/></svg>Videos</div>
      <div class="action"><span class="count">64</span><svg><use href="#i-list"/></svg>Reviews</div>
    </div>
  </article>
</main>

<a class="pill pill-blue abs" style="left:472px;top:2098px;width:256px;height:50px">Show All Playing Movies</a>

<section class="promotions">
  <div class="promo-band"></div>
  <div class="promo-tag">PROMOTIONS</div>
  <div class="promo-poster" role="img" aria-label="Poster for Simply Radiant starring Carly Benning in a pink suit"></div>
  <div class="promo-copy">
    <h3>Simply Radiant</h3>
    <p>Win free tickets to the Ottawa advance screening!</p>
    <a class="pill pill-blue" style="width:115px;height:48px;margin-top:26px">Enter</a>
  </div>
  <div class="promo-arrows">
    <svg width="22" height="14" viewBox="0 0 22 14"><path d="M21 7H2M7 2L2 7l5 5" fill="none" stroke="#9fc7ea" stroke-width="1.6"/></svg>
    <svg width="22" height="14" viewBox="0 0 22 14"><path d="M1 7h19M15 2l5 5-5 5" fill="none" stroke="#9fc7ea" stroke-width="1.6"/></svg>
  </div>
</section>

<h2 class="section-title" style="top:2840px">My Favourite Cinemas</h2>
<p class="fav-sub">No favourite cinemas?</p>
<a class="pill pill-dark abs" style="left:269px;top:2956px;width:323px;height:50px">Log in to retrieve your favourites</a>
<a class="pill pill-blue abs" style="left:611px;top:2956px;width:320px;height:50px">Choose my favourite cinemas</a>

<div class="ad" style="left:377px;background:linear-gradient(135deg,#f4f4f4,#e4e7ea)" role="img" aria-label="Advertisement: business marketing banner with a rocket"></div>
<div class="ad" style="left:614px;background:linear-gradient(160deg,#1b1b1b,#0b0b0b 60%,#3a1212)" role="img" aria-label="Advertisement: seasonal sale banner on black"></div>

<h2 class="section-title" style="top:3428px">Happy Birthday</h2>
<section class="birthday-grid">
  <div class="birthday-card"><div class="avatar" role="img" aria-label="Portrait photo" style="background:#8a7a6c"></div><div><b>Anders Lindqvist</b><span>89 today!</span></div></div>
  <div class="birthday-card"><div class="avatar" role="img" aria-label="Portrait photo" style="background:#7d6656"></div><div><b>Mathieu Laroche</b><span>45 today!</span></div></div>
  <div class="birthday-card"><div class="avatar" role="img" aria-label="Portrait photo" style="background:#5e5148"></div><div><b>Warren Stagg</b><span>66 today!</span></div></div>
  <div class="birthday-card"><div class="avatar" role="img" aria-label="Portrait photo" style="background:#a07a68"></div><div><b>Kelsey Moreland</b><span>34 today!</span></div></div>
  <div class="birthday-card"><div class="avatar" role="img" aria-label="Portrait photo" style="background:#6e6a66"></div><div><b>Dorian Platt</b><span>37 today!</span></div></div>
  <div class="birthday-card"><div class="avatar" role="img" aria-label="Portrait photo" style="background:#4c4a4a"></div><div><b>Toby Ansel Marsh</b><span>30 today!</span></div></div>
  <div class="birthday-card"><div class="avatar" role="img" aria-label="Portrait photo" style="background:#3e4a66"></div><div><b>Reggie Holloway</b><span>50 today!</span></div></div>
  <div class="birthday-card"><div class="avatar" role="img" aria-label="Portrait photo" style="background:#56453d"></div><div><b>Nina Cheng</b><span>35 today!</span></div></div>
  <div class="birthday-card"><div class="avatar" role="img" aria-label="Portrait photo" style="background:#8a6e5a"></div><div><b>Graham Hollis</b><span>43 today!</span></div></div>
</section>

<footer class="site-footer">
  <div class="lang">English &nbsp;|&nbsp; Français</div>
  <div class="copyright">© 1996-2018 Marlo Vista Inc. Terms and Privacy Policy</div>
  <div class="social"><span></span><span></span><span></span><span></span></div>
</footer>

</body>
</html>
```